Professional Services (B-2-B) Business Cards (Front & Back)

Quintarion is a business-to-business professional services company in the legal sector. They typically present to c-suite and executive functions who are looking for providers with expertise, and experience. Our business card should look and feel professional and contemporary, but we are not a startup tech company, so we want the tone to be more mature.

```html
<!DOCTYPE html>
<html lang="en">
<head>
<meta charset="utf-8">
<title>Quintarion Business Cards</title>
<link href="https://fonts.googleapis.com/css2?family=Montserrat:wght@400;500;600&family=Lato:wght@400;700&display=swap" rel="stylesheet">
<style>
  :root {
    --stage: #2b2b2d;
    --navy-deep: #03174a;
    --navy: #082a78;
    --royal: #0b3a8f;
    --streak: #1a4fb8;
    --white: #ffffff;
    --soft-white: #e6ecf8;
  }
  * { margin: 0; padding: 0; box-sizing: border-box; }
  html, body {
    width: 1200px;
    height: 1015px;
    overflow: hidden;
    background: var(--stage);
  }
  .canvas {
    position: relative;
    width: 1200px;
    height: 1015px;
  }
  .card {
    position: absolute;
    width: 560px;
    height: 320px;
    overflow: hidden;
    box-shadow: 0 18px 40px rgba(0,0,0,0.55);
  }
  /* Front */
  .card-front {
    left: 80px;
    top: 110px;
    background: var(--navy-deep);
  }
  .front-texture {
    position: absolute;
    inset: 0;
    background:
      linear-gradient(180deg, transparent 30%, rgba(26,79,184,0.55) 50%, rgba(26,79,184,0.25) 62%, transparent 85%),
      linear-gradient(90deg, var(--navy-deep) 0%, var(--navy) 55%, var(--royal) 100%);
  }
  .front-brand {
    position: absolute;
    left: 0;
    right: 0;
    top: 138px;
    display: flex;
    align-items: center;
    justify-content: center;
    gap: 22px;
  }
  .brand-square {
    width: 34px;
    height: 34px;
    background: var(--white);
  }
  .wordmark {
    font-family: "Montserrat", sans-serif;
    font-weight: 500;
    color: var(--white);
    text-transform: uppercase;
    letter-spacing: 0.42em;
    font-size: 26px;
  }
  /* Back */
  .card-back {
    left: 560px;
    top: 575px;
    background: linear-gradient(135deg, var(--navy) 0%, var(--royal) 100%);
  }
  .back-content {
    position: absolute;
    left: 44px;
    top: 70px;
    color: var(--white);
  }
  .back-content .wordmark {
    font-size: 21px;
    letter-spacing: 0.4em;
  }
  .holder-name {
    margin-top: 34px;
    font-family: "Montserrat", sans-serif;
    font-weight: 600;
    font-size: 21px;
    letter-spacing: 0.02em;
    text-transform: uppercase;
  }
  .holder-title {
    font-family: "Lato", sans-serif;
    font-size: 13px;
    color: var(--soft-white);
    margin-top: 2px;
  }
  .contact-list {
    list-style: none;
    margin-top: 18px;
    font-family: "Lato", sans-serif;
    font-size: 13px;
    line-height: 1.55;
    color: var(--soft-white);
  }
  .contact-list b {
    font-weight: 700;
    color: var(--white);
    margin-right: 4px;
  }
</style>
</head>
<body>
<main class="canvas">
  <section class="card card-front" aria-label="Card front">
    <div class="front-texture" role="img" aria-label="Deep blue background with horizontal light streaks suggesting motion"></div>
    <div class="front-brand">
      <span class="brand-square" aria-hidden="true"></span>
      <span class="wordmark">Quintarion</span>
    </div>
  </section>

  <section class="card card-back" aria-label="Card back">
    <div class="back-content">
      <p class="wordmark">Quintarion</p>
      <h1 class="holder-name">Lena Harrow</h1>
      <p class="holder-title">President &amp; CEO</p>
      <ul class="contact-list">
        <li><b>P:</b>(415) 555-0142</li>
        <li><b>M:</b>(203) 555-0187</li>
        <li><b>E:</b>lharrow@quintarion.tech</li>
        <li><b>W:</b>www.quintarion.tech</li>
      </ul>
    </div>
  </section>
</main>
</body>
</html>
```